Global Translation Company Brochure Design Project

Designers,

“Tessarinth” is a new type of translation agency. We are looking for skilled designers to help us create our first corporate brochure to debut with the opening of our website! Do you have the skills?

(AMENDED)
We have a basic concept that we would like to bring to life (attached). Unfortunately, since we can’t design and we definitely can’t draw, we need YOU to bring this concept to life. As we aim to be a global company bridging the gap between customers and their need for language services, our main graphic element is a globe with words/sentences swirling about it (globesketch.png attached). Our brochure should appeal to the customer and feel professional, eye catching and inviting. We are here to help the customers bridge their language gap for any language.

*** I am willing to accept any design or version of this globe with surrounding text that you feel looks impressive and looks solid. I particularly like the 3D globes. Please feel free to stray from the design in "globe-image.jpg" The goal is to create an impressive image and brochure.

The size and style of this globe is up to you.

EXAMPLE:
The swirling letters/sentences could circle around the front and back of the globe (see the attached “globe-image.jpg”). The style of the words wrapping around the globe is up to you, as long as it is eye-catching.

If possible, please make the text editable (Just in case we decide to change the words swirling around the globe, that is even better).

We are looking for a brochure that is professional, modern, minimalist, and encompasses the colors blue and white (the color and hue are up to you). We have attached our logo, however, feel free to adjust the colors of the logo as necessary.

We would like to see graphic elements that represent the themes that will be included in the brochure: Globalization, Services, Customization, Speed, and Convenience. The scope of work is both the inside brochure design and layout of graphics and text, and the outside brochure design. Requirements for these 2 pages are outlined below.

Please consider the other elements of the brochure as well, as written in the "MUST HAVE" section below.

Feel free to ask questions and I look forward to providing you all constructive feedback on your hard work!

Reason: Due to a craft harbor error, I was unable to upgrade this project to guaranteed. It has been upgraded as of today.

Reason: There is a delay in our responses due to time differences. However, we would like designers to submit their designs/redesigns as soon as possible.

Reason: Due to time differences, we are unable to provide a response within 24 hours. We would like to provide the necessary feedback for creating a successful design.

Reason: Please submit your final changes/designs as soon as possible.

Target Market(s)

Focus on medium to large size businesses but we target individuals and small businesses as well.

Industry/Entity Type

It Company

Requirements
Must have
• - General:
- Dimensions A4 size (however if you think a different size is better, feel free to mention it)
- Use of blue and white as the main colors

(AMENDED)
Inside:
- Placeholder Text (Lorem Ipsum) for the following themes: Globalization (100 words), Services(150 words), Customization(100 words), Speed(100 words), Convenience(100 words)
(I will provide actual text soon. This may help in making choices to add graphics.)
- Graphics that deal with the above themes (a graphic for every theme is not necessary). Please aim for an impressive look and continuity, instead of using many graphics.

-Logo:
Our logo is attached. You are allowed to change the hue and color to make it match the design of the brochure.
(However, please consider the blue and white theme.)

(AMENDED)
Front:
- Use of our logo (attached)
- Tagline "Communicate with the world."

Back:
- Use of our logo

Anywhere:
-Impressive looking globe with words/sentences swirling about it.
(a sketch, globesketch.png, of the basic concept is attached below. Please create an impressive-looking globe as you deem fit.)
(The words I would like to use are attached in a word document: globe design text.doc)

File format:
-InDesign files
-individual files for any graphics added into the brochure
Nice to have
• - Modern minimalist designs expressing a global theme
- Overlapping design from front cover to back cover
- Editable text for the central globe design
Should not have
• - Irrelevant clipart graphics
- Too many images (a minimalist style is better)

```html
<!DOCTYPE html>
<html lang="en">
<head>
<meta charset="utf-8">
<title>Tessarinth – Translation Services</title>
<link rel="stylesheet" href="https://fonts.googleapis.com/css2?family=Exo+2:wght@300;400;600;700&display=swap">
<style>
  :root {
    --sky-light: #3fb4ee;
    --sky-mid: #1a8fdb;
    --sky-deep: #0a66bf;
    --panel-white: #ffffff;
    --panel-blue: #0a5db0;
    --ink-blue: #1564b6;
    --text-white: #ffffff;
    --globe-light: #eef7fd;
    --globe-mid: #9fd0f2;
    --globe-deep: #2a82d0;
  }
  * { margin: 0; padding: 0; box-sizing: border-box; }
  html, body { width: 871px; height: 1200px; overflow: hidden; background: #ffffff; }
  .sheet {
    position: relative;
    width: 871px;
    height: 1200px;
    overflow: hidden;
    font-family: "Exo 2", sans-serif;
    background:
      radial-gradient(ellipse 520px 300px at 680px 200px, rgba(255,255,255,0.22), rgba(255,255,255,0) 70%),
      linear-gradient(180deg, var(--sky-light) 0%, var(--sky-mid) 45%, var(--sky-deep) 100%);
  }
  .wave-band {
    position: absolute;
    left: 0; top: 0;
    width: 871px; height: 1200px;
  }
  .globe-visual {
    position: absolute;
    left: -88px; top: 612px;
    width: 640px; height: 640px;
    border-radius: 50%;
    background: radial-gradient(circle at 38% 30%, var(--globe-light) 0%, var(--globe-mid) 42%, var(--globe-deep) 100%);
  }
  .intro-panel {
    position: absolute;
    left: 114px; top: 43px;
    width: 634px; height: 444px;
    background: var(--panel-white);
    border-radius: 12px 60px 10px 74px;
  }
  .intro-title {
    position: absolute;
    left: 0; top: 52px;
    width: 634px;
    text-align: center;
    font-size: 42px;
    font-weight: 300;
    color: var(--ink-blue);
    letter-spacing: 0.2px;
  }
  .intro-copy {
    position: absolute;
    left: 79px; top: 138px;
    width: 476px;
    font-size: 16.2px;
    line-height: 29px;
    font-weight: 700;
    color: var(--ink-blue);
    text-align: justify;
    hyphens: auto;
    -webkit-hyphens: auto;
  }
  .intro-tagline {
    position: absolute;
    left: 0; top: 303px;
    width: 634px;
    text-align: center;
    font-size: 28.5px;
    line-height: 34px;
    font-weight: 700;
    color: var(--ink-blue);
  }
  .wave-panel {
    position: absolute;
    left: 286px; top: 502px;
    width: 520px; height: 378px;
    background: var(--panel-blue);
    border-radius: 54px 48px 12px 70px;
  }
  .wave-title {
    position: absolute;
    left: 48px; top: 50px;
    font-size: 27px;
    font-weight: 300;
    color: var(--text-white);
  }
  .wave-copy {
    position: absolute;
    left: 51px; top: 121px;
    width: 424px;
    font-size: 13.8px;
    line-height: 18.3px;
    font-weight: 400;
    letter-spacing: 0.9px;
    color: var(--text-white);
    text-align: justify;
    hyphens: auto;
    -webkit-hyphens: auto;
  }
  .footer-rule {
    position: absolute;
    left: 473px; top: 1152px;
    width: 228px; height: 2px;
    background: var(--text-white);
  }
  .brand-name {
    position: absolute;
    left: 716px; top: 1151px;
    font-size: 23px;
    line-height: 1;
    font-weight: 600;
    color: var(--text-white);
    transform: translateY(-50%);
  }
</style>
</head>
<body>
  <main class="sheet">
    <svg class="wave-band" viewBox="0 0 871 1200" aria-hidden="true">
      <path d="M0 300 Q 430 150 871 250 L 871 520 Q 430 400 0 560 Z" fill="#ffffff" opacity="0.06"/>
    </svg>

    <div class="globe-visual" role="img" aria-label="Glowing blue and white 3D globe wrapped by sweeping translucent ribbons"></div>

    <section class="intro-panel">
      <h1 class="intro-title">Welcome to Tessarinth</h1>
      <p class="intro-copy">Specializing in all forms of translation, we provide the services that you need to put your documents into another language. However, we do not just translate-we recreate your thoughts on the page in the language of your choice. Whether you want to put your content into Japanese or English, you’ve come to the right place.</p>
      <p class="intro-tagline">We ensure your words<br>say what you mean</p>
    </section>

    <section class="wave-panel">
      <h2 class="wave-title">Riding the globalization wave</h2>
      <p class="wave-copy">Today, being global is more important than it has ever been, calling for the need to make your services available in more than just one language. Increase your customer base, provide global customer service, impress foreign clients, or simply have a multi-lingual presence on the web. Tessarinth has all the resources necessary for turning your company into a one-stop shop for speakers of any language. Let us help you show the world how truly global you are. Tessarinth- providing you with a brilliant translation, each and every time.</p>
    </section>

    <div class="footer-rule"></div>
    <div class="brand-name">Tessarinth</div>
  </main>
</body>
</html>
```